Flyer to acquire new customers for a craft business

Create an A5 (4 pages in total) flyer describing proposed services from a craft business to new customers.

Services are :

All types of renovation (painting, plastering, attaching wallpapers ....)
All types of repairs
Electric repairs
Little to medium woodworks
Services around the house and garden

Flyer must be translatable into several languages beginning with FRENCH.
Texts are being written by ourselves.

Target Market(s)

Private customers

Industry/Entity Type

Mixed craft business

Colors

Designer to choose colors to be used in the design.

```html
<!DOCTYPE html>
<html lang="fr">
<head>
<meta charset="utf-8">
<title>Brikolo – Flyer A5</title>
<link rel="stylesheet" href="https://fonts.googleapis.com/css2?family=Montserrat:wght@400;500;600;700;800;900&display=swap">
<style>
  :root {
    --navy: #2e2856;
    --navy-deep: #28224d;
    --gold: #e9b95a;
    --gold-soft: #f0cf8e;
    --cream: #fbf1e3;
    --paper: #ffffff;
    --ink: #2e2856;
    --body-ink: #3b3950;
    --backdrop: #4e504d;
  }
  * { margin: 0; padding: 0; box-sizing: border-box; }
  html, body {
    width: 1200px; height: 1200px; overflow: hidden;
    background: var(--backdrop);
    font-family: "Montserrat", sans-serif;
  }
  .spread { position: relative; width: 1200px; height: 1200px; }
  .page {
    position: absolute; top: 245px;
    width: 684px; height: 970px;
    background: var(--paper);
    transform: scale(0.731); transform-origin: 0 0;
    overflow: hidden;
  }
  .page--inside { left: 80px; }
  .page--cover { left: 620px; }
  .page > svg.backdrop { position: absolute; inset: 0; width: 684px; height: 970px; }

  /* inside page */
  .pitch {
    position: absolute; left: 46px; top: 586px; width: 272px;
    color: var(--body-ink);
  }
  .pitch__title { font-weight: 700; font-size: 19.5px; line-height: 27px; color: var(--ink); margin-bottom: 6px; }
  .pitch__item { font-weight: 400; font-size: 19px; line-height: 27px; margin-bottom: 8px; }
  .contact { position: absolute; left: 386px; top: 658px; list-style: none; }
  .contact li {
    display: flex; align-items: center; gap: 11px;
    height: 29.5px; font-weight: 700; font-size: 16px; color: var(--ink);
  }
  .contact svg { width: 16px; height: 16px; flex: none; }

  .brand { position: absolute; display: flex; align-items: center; gap: 20px; }
  .brand__mark { border-radius: 50%; background: var(--navy); flex: none; }
  .brand__name { font-weight: 800; color: var(--navy); letter-spacing: 0.5px; }
  .brand--inside { left: 375px; top: 815px; }
  .brand--inside .brand__mark { width: 96px; height: 96px; }
  .brand--inside .brand__name { font-size: 30px; }
  .brand--cover { left: 198px; top: 34px; }
  .brand--cover .brand__mark { width: 106px; height: 106px; }
  .brand--cover .brand__name { font-size: 34px; }

  /* cover page */
  .headline {
    position: absolute; left: 0; right: 0; top: 180px;
    text-align: center; color: var(--ink);
    font-weight: 800; font-size: 76px; line-height: 72px; letter-spacing: -1px;
  }
  .services {
    position: absolute; left: 0; right: 0; top: 768px;
    list-style: none; text-align: center;
    color: var(--gold); font-weight: 800; font-size: 25px;
  }
  .services li { height: 54.5px; line-height: 54.5px; }
</style>
</head>
<body>
<main class="spread">

  <!-- Inside page -->
  <section class="page page--inside">
    <svg class="backdrop" viewBox="0 0 684 970">
      <defs>
        <linearGradient id="workPhoto" x1="0" y1="0" x2="1" y2="1">
          <stop offset="0" stop-color="#f3dfb6"/>
          <stop offset="0.55" stop-color="#c9a98a"/>
          <stop offset="1" stop-color="#6a6470"/>
        </linearGradient>
      </defs>
      <polygon points="683,425 683,710 290,940 0,940 0,825" fill="var(--cream)"/>
      <polygon points="0,0 683,0 683,425 500,527 0,527" fill="url(#workPhoto)"
               role="img" aria-label="Photo d'un artisan démontant un vieux parquet avec un marteau et un pied-de-biche"/>
      <rect x="0" y="940" width="684" height="30" fill="var(--navy)"/>
      <rect x="372" y="942" width="312" height="9" fill="var(--gold)"/>
      <path d="M26,572 H324 V680 L359,704 L324,728 V879 H26 Z" fill="var(--paper)" stroke="var(--gold)" stroke-width="8" stroke-linejoin="miter"/>
    </svg>

    <div class="pitch">
      <p class="pitch__title">Vous êtes à la recherche d'un partenaire fiable ?</p>
      <p class="pitch__item">Pour tous types de travaux et de services de l'artisanat</p>
      <p class="pitch__item">Petits, moyens ou plus grands projets</p>
      <p class="pitch__item">Intervention rapide</p>
      <p class="pitch__item">Contactez-nous pour un conseil personnalisé</p>
    </div>

    <ul class="contact">
      <li>
        <svg viewBox="0 0 16 16"><circle cx="8" cy="8" r="7.5" fill="var(--navy)"/><path d="M5.3 4.2l1.3-.3.8 1.9-.9.7c.5 1 1.2 1.7 2.2 2.2l.7-.9 1.9.8-.3 1.3c-3.4.2-5.9-2.3-5.7-5.7z" fill="#fff"/></svg>
        +352 26 40 18 75
      </li>
      <li>
        <svg viewBox="0 0 16 16" fill="none" stroke="var(--navy)" stroke-width="1.3"><circle cx="8" cy="8" r="6.5"/><ellipse cx="8" cy="8" rx="2.8" ry="6.5"/><path d="M1.5 8h13M2.5 4.8h11M2.5 11.2h11"/></svg>
        www.brikolo.lu
      </li>
      <li>
        <svg viewBox="0 0 16 16"><rect x="0.5" y="3" width="15" height="10" fill="var(--navy)"/><path d="M1 3.5l7 5.5 7-5.5M1 12.5l5-4.5M15 12.5l-5-4.5" stroke="#fff" stroke-width="1.1" fill="none"/></svg>
        info@brikolo.lu
      </li>
    </ul>

    <div class="brand brand--inside">
      <span class="brand__mark"></span>
      <span class="brand__name">Brikolo</span>
    </div>
  </section>

  <!-- Cover page -->
  <section class="page page--cover">
    <svg class="backdrop" viewBox="0 0 684 970">
      <defs>
        <linearGradient id="stripeTone" x1="0" y1="0" x2="1" y2="0">
          <stop offset="0" stop-color="#f7e4c0"/>
          <stop offset="1" stop-color="#ecc681"/>
        </linearGradient>
        <linearGradient id="paintPhoto" x1="0" y1="0" x2="1" y2="1">
          <stop offset="0" stop-color="#c98a4c"/>
          <stop offset="0.5" stop-color="#3f6f73"/>
          <stop offset="1" stop-color="#efb63b"/>
        </linearGradient>
        <linearGradient id="toolPhoto" x1="0" y1="0" x2="1" y2="1">
          <stop offset="0" stop-color="#d9b59c"/>
          <stop offset="0.45" stop-color="#3a3d44"/>
          <stop offset="1" stop-color="#15171c"/>
        </linearGradient>
      </defs>
      <g fill="url(#stripeTone)">
        <polygon points="0,880 683,505 683,525 0,900" opacity="1"/>
        <polygon points="0,845 683,470 683,492 0,867"/>
        <polygon points="0,810 683,435 683,457 0,832"/>
        <polygon points="0,775 683,400 683,422 0,797" opacity="0.95"/>
        <polygon points="0,740 683,365 683,386 0,761" opacity="0.85"/>
        <polygon points="0,705 683,330 683,350 0,725" opacity="0.75"/>
        <polygon points="0,670 683,295 683,314 0,689" opacity="0.6"/>
        <polygon points="0,635 683,260 683,278 0,653" opacity="0.5"/>
        <polygon points="0,600 683,225 683,241 0,616" opacity="0.4"/>
        <polygon points="0,565 683,190 683,204 0,579" opacity="0.3"/>
        <polygon points="0,530 683,155 683,167 0,542" opacity="0.22"/>
        <polygon points="0,495 683,120 683,130 0,505" opacity="0.15"/>
      </g>
      <polygon points="0,893 683,518 683,970 0,970" fill="var(--navy)"/>
      <g stroke="var(--navy-deep)" stroke-width="6" opacity="0.6">
        <line x1="0" y1="930" x2="683" y2="555"/>
        <line x1="0" y1="960" x2="683" y2="585"/>
        <line x1="0" y1="990" x2="683" y2="615"/>
      </g>
      <polygon points="201,444 340,524 340,684 201,764 62,684 62,524"
               fill="url(#paintPhoto)" stroke="var(--paper)" stroke-width="9"
               role="img" aria-label="Photo d'outils de peinture : rouleaux, pinceaux, bac et gants sur un parquet"/>
      <polygon points="483,354 626,437 626,601 483,684 340,601 340,437"
               fill="url(#toolPhoto)" stroke="var(--paper)" stroke-width="9"
               role="img" aria-label="Photo d'une main tenant des clés plates devant une caisse à outils"/>
    </svg>

    <div class="brand brand--cover">
      <span class="brand__mark"></span>
      <span class="brand__name">Brikolo</span>
    </div>

    <h1 class="headline">Ären<br>Handwierker</h1>

    <ul class="services">
      <li>Rénovations</li>
      <li>Réparations</li>
      <li>Tous types de services de l'artisanat</li>
    </ul>
  </section>

</main>
</body>
</html>
```